Business Card for Orthopaedic Clinic.
Should have nice design, double sided that includes logo
Should include my name, my contact, my email, webpage. A QR code to scan business card.

please use dummy information for privacy reasons. I will provide my name, email, practice address once a winner is selected.

Target Market(s)

Future patients

Contact Information for Business Card

Name: Dr Ruk
Contact No: +65 90417263
Practice Address: Singapore
Email: doctor@brevlo.com
Website: www.brevlo.com

Colors
00a990

Requirements
Must have
• Logo and a nice colour scheme.
A QR Code for Contact Card.
Name
Contact
Practice Address
Email
Website.
Nice to have
• Nice colour scheme
Should not have
• Nothing too cluttered.

```html
<!DOCTYPE html>
<html lang="en">
<head>
<meta charset="utf-8">
<title>Brevlo Orthopaedics – Business Card</title>
<link href="https://fonts.googleapis.com/css2?family=Abel&family=Questrial&family=Roboto:wght@900&display=swap" rel="stylesheet">
<style>
  :root {
    --stage: #000000;
    --paper: #ffffff;
    --teal: #139b8b;
    --teal-soft: #5fb096;
    --stone: #aeaba4;
    --ink: #4a4a55;
    --black: #111111;
  }
  * { box-sizing: border-box; margin: 0; padding: 0; }
  html, body {
    width: 939px; height: 1200px; overflow: hidden;
    background: var(--stage);
  }
  .card {
    position: absolute;
    left: 61px; width: 823px; height: 480px;
    background: var(--paper);
    overflow: hidden;
  }
  .card--front { top: 67px; }
  .card--back { top: 651px; }

  /* brand block */
  .brand {
    position: absolute;
    display: flex; flex-direction: column; align-items: center;
    font-family: "Questrial", sans-serif;
    color: var(--ink);
    font-weight: 400;
  }
  .brand__mark {
    background: var(--teal-soft);
    border-radius: 10px;
  }
  .brand__name { line-height: 1; letter-spacing: 2px; }
  .brand__sub { line-height: 1; }

  .card--front .brand { left: 27px; width: 400px; top: 95px; }
  .card--front .brand__mark { width: 92px; height: 92px; margin-bottom: 22px; }
  .card--front .brand__name { font-size: 56px; }
  .card--front .brand__sub { font-size: 27px; margin-top: 8px; letter-spacing: 14px; padding-left: 14px; }

  .card--back .brand { left: 192px; width: 500px; top: 66px; }
  .card--back .brand__mark { width: 108px; height: 108px; margin-bottom: 26px; }
  .card--back .brand__name { font-size: 68px; }
  .card--back .brand__sub { font-size: 33px; margin-top: 8px; letter-spacing: 16px; padding-left: 16px; }

  /* contact panel */
  .contact-panel {
    position: absolute; right: 0; top: 0;
    width: 391px; height: 480px;
    background: var(--teal);
    border-bottom-left-radius: 110px;
  }
  .contact-panel__name {
    position: absolute; left: 86px; top: 36px;
    font-family: "Roboto", sans-serif; font-weight: 900;
    font-size: 32px; color: var(--black);
  }
  .contact-list { list-style: none; }
  .contact-item {
    position: absolute; left: 78px;
    display: flex; align-items: center;
    font-family: "Abel", sans-serif;
    font-size: 33px; color: var(--black);
    white-space: nowrap;
  }
  .contact-item__icon {
    width: 46px; height: 46px; margin-right: 13px; flex: none;
  }
  .contact-item--phone { top: 148px; }
  .contact-item--place { top: 223px; }
  .contact-item--mail  { top: 305px; font-size: 32px; }
  .contact-item--web   { top: 377px; }

  .back-swoosh {
    position: absolute; left: 0; bottom: 0;
    width: 823px; height: 110px;
  }
  .contact-qr {
    position: absolute; right: 34px; bottom: 12px;
    width: 86px; height: 86px;
    background: var(--paper);
    border: 6px solid var(--paper);
    border-radius: 6px;
    box-shadow: inset 0 0 0 3px var(--black);
  }
</style>
</head>
<body>

<section class="card card--front">
  <div class="brand">
    <div class="brand__mark"></div>
    <div class="brand__name">BREVLO</div>
    <div class="brand__sub">ORTHOPAEDICS</div>
  </div>

  <div class="contact-panel">
    <div class="contact-panel__name">Dr Ruk</div>
    <ul class="contact-list">
      <li class="contact-item contact-item--phone">
        <svg class="contact-item__icon" viewBox="0 0 40 40" aria-hidden="true">
          <rect x="12" y="2" width="16" height="36" rx="3" fill="none" stroke="#111" stroke-width="3"/>
          <circle cx="20" cy="33" r="2" fill="#111"/>
        </svg>
        <span>+65 90417263</span>
      </li>
      <li class="contact-item contact-item--place">
        <svg class="contact-item__icon" viewBox="0 0 40 40" aria-hidden="true">
          <path d="M20 3a11 11 0 0 0-11 11c0 8 11 20 11 20s11-12 11-20A11 11 0 0 0 20 3z" fill="#111"/>
          <circle cx="20" cy="14" r="4.5" fill="#139b8b"/>
          <ellipse cx="20" cy="36" rx="9" ry="2.5" fill="#111"/>
        </svg>
        <span>Singapore</span>
      </li>
      <li class="contact-item contact-item--mail">
        <svg class="contact-item__icon" viewBox="0 0 40 40" aria-hidden="true">
          <rect x="3" y="14" width="34" height="22" fill="#111"/>
          <path d="M3 14l17 13 17-13" fill="none" stroke="#139b8b" stroke-width="2"/>
          <rect x="11" y="5" width="18" height="14" fill="#fff" stroke="#111" stroke-width="1.5"/>
          <text x="20" y="16" font-size="10" text-anchor="middle" font-family="sans-serif" fill="#111">@</text>
        </svg>
        <span>doctor@brevlo.com</span>
      </li>
      <li class="contact-item contact-item--web">
        <svg class="contact-item__icon" viewBox="0 0 40 40" aria-hidden="true" fill="none" stroke="#111" stroke-width="2">
          <circle cx="20" cy="20" r="16"/>
          <ellipse cx="20" cy="20" rx="7" ry="16"/>
          <path d="M4 20h32M6 12h28M6 28h28M20 4v32"/>
        </svg>
        <span>www.brevlo.com</span>
      </li>
    </ul>
  </div>
</section>

<section class="card card--back">
  <div class="brand">
    <div class="brand__mark"></div>
    <div class="brand__name">BREVLO</div>
    <div class="brand__sub">ORTHOPAEDICS</div>
  </div>

  <svg class="back-swoosh" viewBox="0 0 823 110" aria-hidden="true">
    <path d="M117 110C130 60 175 23 250 23H420V110Z" fill="var(--stone)"/>
    <path d="M226 110C240 40 300 0 390 0H823V110Z" fill="var(--teal)"/>
  </svg>
  <div class="contact-qr" role="img" aria-label="QR code linking to the digital contact card"></div>
</section>

</body>
</html>
```